Flyer for local business that installs fences and sells fence materials

We recently began selling fence materials, in addition to also doing fence installations. We need a flyer that displays our business information and photos of our work, as well as a flyer that shows customers they have the option to buy materials only also.

If they are looking to build a fence - we can help by installing it, or if they want to install themselves, they can buy the materials only from us too. We provide a lifetime warranty on all materials and installations. More information about the company is here: www.BrambleRailWorks.com

Its important to have the company logo, phone number, email and business hours listed (Monday - Thursday 9AM - 3PM, Friday 9AM - 1PM).

It is also important to show the fence material types we offer:
Wood, Chainlink, Vinyl and Aluminum
Updates

Updated with more photos and url to website www.bramblerailworks.com for details

Target Market(s)

Residential Homeowners

Industry/Entity Type

Construction

Font styles to use
Sans Serif
Other font styles liked:
• Arial

Colors
0054AA
0677BA
7BADD7
CADEEF
E8F1F8

Requirements
Must have
• Photos of the fencing we offer
Nice to have
• A way to explain to customers they can hire us to install, or just buy the materials from us
Should not have
• Too many colors or too many words

```html
<!DOCTYPE html>
<html lang="en">
<head>
<meta charset="utf-8">
<title>Bramble Rail Works – Fence Flyer</title>
<link rel="stylesheet" href="https://fonts.googleapis.com/css2?family=Archivo:wght@700;800;900&family=Montserrat:wght@400;500;700&family=Oswald:wght@500&display=swap">
<style>
  :root {
    --orange: #e8953a;
    --orange-deep: #c97a22;
    --orange-soft: #eda24c;
    --ink: #0c0c0c;
    --white: #ffffff;
    --blue: #3a80c6;
    --brown: #5a3a26;
    --photo-sky: #3b67b8;
    --photo-grass: #5d6f3a;
  }
  * { box-sizing: border-box; margin: 0; padding: 0; }
  html, body { width: 920px; height: 1200px; overflow: hidden; background: #d4d4d4; }
  .flyer { position: relative; width: 920px; height: 1200px; font-family: "Montserrat", Arial, sans-serif; }
  .hero {
    position: absolute; inset: 0 0 180px 0;
    background:
      radial-gradient(ellipse at 30% 25%, var(--orange-deep) 0%, transparent 55%),
      radial-gradient(ellipse at 75% 70%, #d5852c 0%, transparent 50%),
      linear-gradient(180deg, var(--orange) 0%, var(--orange-soft) 100%);
  }
  .headline {
    position: absolute; left: 57px; top: 42px;
    font-family: "Archivo", Arial, sans-serif; font-weight: 900;
    font-size: 86px; line-height: 87px; letter-spacing: -1px; color: var(--white);
    transform: scaleX(1.33); transform-origin: left top; white-space: nowrap;
  }
  .headline .dark { color: var(--ink); }
  .subline { position: absolute; left: 57px; top: 304px; font-size: 31px; line-height: 37px; color: var(--white); white-space: nowrap; }
  .offer-title {
    position: absolute; left: 50px; top: 410px;
    font-family: "Archivo", Arial, sans-serif; font-weight: 900;
    font-size: 33px; line-height: 36px; color: var(--ink); letter-spacing: -0.5px;
    transform: scaleX(1.28); transform-origin: left top; white-space: nowrap;
  }
  .offer-list { position: absolute; left: 50px; top: 452px; list-style: none; }
  .offer-list li { display: flex; align-items: center; height: 29px; font-size: 22px; color: var(--white); white-space: nowrap; }
  .offer-list svg { width: 17px; height: 17px; margin-right: 15px; flex: none; }
  .offer-list .highlight { font-weight: 700; }
  .free-note {
    position: absolute; left: 50px; top: 752px;
    font-weight: 700; color: var(--white);
    font-size: 36px; line-height: 36px;
  }
  .free-note .big { display: block; font-family: "Archivo", Arial, sans-serif; font-weight: 900; font-size: 66px; line-height: 66px; margin-left: -3px; }
  .timing-tag {
    position: absolute; left: 50px; top: 912px; width: 108px; height: 26px;
    background: var(--ink); color: var(--white); font-weight: 700; font-size: 19px;
    line-height: 26px; padding-left: 6px;
    clip-path: polygon(0 0, 92% 0, 100% 50%, 92% 100%, 0 100%);
  }
  .hours { position: absolute; left: 50px; top: 944px; font-size: 19px; line-height: 28px; color: var(--white); }
  .photo-frame { position: absolute; left: 585px; width: 290px; height: 268px; background: var(--white); padding: 16px 17px; }
  .photo-frame .photo { width: 100%; height: 100%; }
  .frame-vinyl { top: 55px; }
  .frame-chain { top: 371px; }
  .frame-wood { top: 688px; }
  .photo-vinyl { background: linear-gradient(180deg, var(--photo-sky) 0%, #8aa4d4 30%, #e9e9ec 45%, #cfd0d3 70%, var(--photo-grass) 100%); }
  .photo-chain { background: linear-gradient(180deg, #9c8d7a 0%, #a7a9a4 30%, #6f7a52 70%, #4f5e34 100%); }
  .photo-wood { background: linear-gradient(180deg, #30402a 0%, #4b5b34 35%, #c9b07a 55%, #4e5a31 100%); }
  .footer { position: absolute; left: 0; right: 0; bottom: 0; height: 180px; background: var(--white); }
  .brand-mark { position: absolute; left: 48px; top: 50px; width: 72px; height: 72px; background: var(--brown); }
  .brand-name {
    position: absolute; left: 155px; top: 38px;
    font-family: "Archivo", Arial, sans-serif; font-weight: 900;
    font-size: 28px; color: var(--blue); white-space: nowrap;
  }
  .brand-phone {
    position: absolute; left: 155px; top: 80px;
    font-family: "Archivo", Arial, sans-serif; font-weight: 900;
    font-size: 30px; color: var(--ink); white-space: nowrap;
    transform: scaleX(1.26); transform-origin: left top;
  }
  .brand-tagline {
    position: absolute; left: 156px; top: 122px;
    font-family: "Archivo", Arial, sans-serif; font-weight: 800; font-size: 10.5px; color: var(--ink); white-space: nowrap;
  }
  .divider { position: absolute; left: 503px; top: 30px; width: 2px; height: 122px; background: var(--brown); }
  .contact { position: absolute; right: 40px; top: 40px; text-align: right; }
  .contact-label { font-weight: 700; font-size: 16px; line-height: 20px; color: var(--ink); }
  .contact-phone { font-family: "Oswald", Arial, sans-serif; font-weight: 500; font-size: 64px; line-height: 64px; color: var(--blue); letter-spacing: -1px; }
  .contact-web, .contact-email { font-weight: 700; font-size: 15px; line-height: 19px; color: var(--ink); }
</style>
</head>
<body>
<div class="flyer">
  <div class="hero" role="img" aria-label="Orange-tinted background photo of trees and a black aluminum picket fence"></div>

  <h1 class="headline">WE<br><span class="dark">BUILD</span><br>FENCE</h1>
  <p class="subline">and we would love to build<br>your fence too!</p>

  <h2 class="offer-title">WE OFFER</h2>
  <ul class="offer-list">
    <li><svg viewBox="0 0 20 20"><circle cx="10" cy="10" r="8" fill="none" stroke="#0c0c0c" stroke-width="2.6"/><path d="M5.5 10l3.5 3.5L19 3.5" fill="none" stroke="#0c0c0c" stroke-width="2.8"/></svg>Free Estimate</li>
    <li><svg viewBox="0 0 20 20"><circle cx="10" cy="10" r="8" fill="none" stroke="#0c0c0c" stroke-width="2.6"/><path d="M5.5 10l3.5 3.5L19 3.5" fill="none" stroke="#0c0c0c" stroke-width="2.8"/></svg>Proffesional Installation</li>
    <li class="highlight"><svg viewBox="0 0 20 20"><circle cx="10" cy="10" r="8" fill="none" stroke="#0c0c0c" stroke-width="2.6"/><path d="M5.5 10l3.5 3.5L19 3.5" fill="none" stroke="#0c0c0c" stroke-width="2.8"/></svg>Or Buy Materials Only</li>
    <li class="highlight"><svg viewBox="0 0 20 20"><circle cx="10" cy="10" r="8" fill="none" stroke="#0c0c0c" stroke-width="2.6"/><path d="M5.5 10l3.5 3.5L19 3.5" fill="none" stroke="#0c0c0c" stroke-width="2.8"/></svg>Wood, Chainlink, Vinyl &amp; Aluminum</li>
    <li><svg viewBox="0 0 20 20"><circle cx="10" cy="10" r="8" fill="none" stroke="#0c0c0c" stroke-width="2.6"/><path d="M5.5 10l3.5 3.5L19 3.5" fill="none" stroke="#0c0c0c" stroke-width="2.8"/></svg>Concrete in Every Post</li>
    <li><svg viewBox="0 0 20 20"><circle cx="10" cy="10" r="8" fill="none" stroke="#0c0c0c" stroke-width="2.6"/><path d="M5.5 10l3.5 3.5L19 3.5" fill="none" stroke="#0c0c0c" stroke-width="2.8"/></svg>HOA Submission Assistance</li>
    <li><svg viewBox="0 0 20 20"><circle cx="10" cy="10" r="8" fill="none" stroke="#0c0c0c" stroke-width="2.6"/><path d="M5.5 10l3.5 3.5L19 3.5" fill="none" stroke="#0c0c0c" stroke-width="2.8"/></svg>Lifetime Workmanshop Warranty</li>
    <li><svg viewBox="0 0 20 20"><circle cx="10" cy="10" r="8" fill="none" stroke="#0c0c0c" stroke-width="2.6"/><path d="M5.5 10l3.5 3.5L19 3.5" fill="none" stroke="#0c0c0c" stroke-width="2.8"/></svg>Experienced Installation Teams</li>
    <li><svg viewBox="0 0 20 20"><circle cx="10" cy="10" r="8" fill="none" stroke="#0c0c0c" stroke-width="2.6"/><path d="M5.5 10l3.5 3.5L19 3.5" fill="none" stroke="#0c0c0c" stroke-width="2.8"/></svg>Quality Workmanship &amp; Materials</li>
    <li><svg viewBox="0 0 20 20"><circle cx="10" cy="10" r="8" fill="none" stroke="#0c0c0c" stroke-width="2.6"/><path d="M5.5 10l3.5 3.5L19 3.5" fill="none" stroke="#0c0c0c" stroke-width="2.8"/></svg>Free Gate Adjustments for Life</li>
  </ul>

  <p class="free-note">ESTIMATE<br>ARE ALWAYS<span class="big">FREE</span></p>

  <div class="timing-tag">TIMING</div>
  <p class="hours">Monday - Thursday 9AM - 3PM,<br>Friday 9AM - 1PM).</p>

  <figure class="photo-frame frame-vinyl"><div class="photo photo-vinyl" role="img" aria-label="Photo of a white vinyl privacy fence along a row of houses"></div></figure>
  <figure class="photo-frame frame-chain"><div class="photo photo-chain" role="img" aria-label="Photo of a new chain-link fence across a grassy yard"></div></figure>
  <figure class="photo-frame frame-wood"><div class="photo photo-wood" role="img" aria-label="Photo of an installer building a wooden privacy fence"></div></figure>

  <footer class="footer">
    <div class="brand-mark"></div>
    <div class="brand-name">Bramble Rail Works</div>
    <div class="brand-phone">704-555-0148</div>
    <div class="brand-tagline">“Because Good Fences Make Good Neighbors”</div>
    <div class="divider"></div>
    <div class="contact">
      <div class="contact-label">CONTACT US NOW!</div>
      <div class="contact-phone">704-555-0148</div>
      <div class="contact-web">www.bramblerailworks.com</div>
      <div class="contact-email">info@bramblerailworks.com</div>
    </div>
  </footer>
</div>
</body>
</html>
```